VELKA Natural Hair Care Products

We need a design of label(s) for our natural hair care products for ethnic hair.The products are made of natural ingredients,we would like to see designs that convey a clean and portray a natural feel.
VELKA Hair Shampoo - label size 120mm x120mm
VELKA Hair Moisturiser - label size 200mm x 25mm
VELKA Softener Spray - label size 120mm x120mm

Target Market(s)

Black women with natural hair
High income earners
Natural/Organic market

Industry/Entity Type

Hair

Colors

Designer to choose colors to be used in the design.

Requirements
Must have
• A natural/organic feel or colours

```html
<!DOCTYPE html>
<html lang="en">
<head>
<meta charset="utf-8">
<title>VELKA Natural Hair Care Labels</title>
<link href="https://fonts.googleapis.com/css2?family=Oswald:wght@300;500&display=swap" rel="stylesheet">
<style>
  :root {
    --canvas: #f4f2f3;
    --ink: #111111;
    --band: #0c0c0c;
    --pink: #ff1d80;
    --coral: #ff5a4a;
    --orange: #ff9a1a;
    --yellow: #ffe100;
  }
  * { box-sizing: border-box; margin: 0; padding: 0; }
  html, body { width: 1200px; height: 843px; overflow: hidden; }
  body {
    background: var(--canvas);
    font-family: "Oswald", "Arial Narrow", sans-serif;
    color: var(--ink);
    position: relative;
  }
  .label {
    position: absolute;
    background:
      radial-gradient(circle at 95% 10%, var(--yellow) 0%, rgba(255,225,0,0) 55%),
      linear-gradient(215deg, var(--yellow) 0%, var(--orange) 40%, var(--coral) 62%, var(--pink) 88%);
    border-top: 10px solid var(--band);
    border-bottom: 10px solid var(--band);
    text-align: center;
    text-transform: uppercase;
  }
  .label--square { width: 320px; height: 320px; top: 110px; }
  .label--shampoo { left: 200px; }
  .label--spray { left: 680px; }
  .label--strip {
    left: 200px; top: 560px; width: 800px; height: 112px;
    border-top-width: 8px; border-bottom-width: 8px;
    display: flex; flex-direction: column; align-items: center; justify-content: center;
  }
  .brand {
    font-weight: 300;
    font-size: 34px;
    letter-spacing: 4px;
    color: var(--ink);
  }
  .label--square .brand { margin-top: 72px; }
  .product-name {
    font-weight: 500;
    font-size: 19px;
    letter-spacing: 0.3px;
    margin-top: 50px;
  }
  .details {
    font-weight: 500;
    font-size: 13px;
    line-height: 1.7;
    margin-top: 52px;
  }
  .label--spray .brand { margin-top: 60px; }
  .label--spray .product-name { margin-top: 56px; }
  .label--spray .details { margin-top: 58px; }
  .label--strip .brand { font-size: 24px; line-height: 1; }
  .label--strip .product-name { font-size: 18px; margin-top: 6px; line-height: 1.1; }
  .label--strip .details { font-size: 10px; line-height: 1.5; margin-top: 6px; }
</style>
</head>
<body>
  <section class="label label--square label--shampoo" aria-label="VELKA Hair Shampoo label">
    <p class="brand">VELKA</p>
    <h2 class="product-name">2 in 1 Shampoo</h2>
    <p class="details">With olive and peppermint oil<br>Cleansing and conditioning</p>
  </section>

  <section class="label label--square label--spray" aria-label="VELKA Softener Spray label">
    <p class="brand">VELKA</p>
    <h2 class="product-name">Hair Softener Spray</h2>
    <p class="details">With orange oil<br>Daily care and softening</p>
  </section>

  <section class="label label--strip" aria-label="VELKA Hair Moisturiser label">
    <p class="brand">VELKA</p>
    <h2 class="product-name">Hair Moisturizer</h2>
    <p class="details">With cinnamon oil<br>Helps with strengthening and anti-breakage</p>
  </section>
</body>
</html>
```